BrightLoopDeals

I need 4 thumbnails for the website area "How It Works". Sizes of thumbnails should be 400x290px. Something that reflects the steps and suits the rest of the site brightloopdeals.com design

```html
<!DOCTYPE html>
<html lang="en">
<head>
<meta charset="utf-8">
<title>BrightLoopDeals – How It Works</title>
<link rel="stylesheet" href="https://fonts.googleapis.com/css2?family=Lexend:wght@400;500;600&family=Inter:wght@400;500&display=swap">
<style>
  :root {
    --page-bg: #f7f8fc;
    --white: #ffffff;
    --ink: #111111;
    --muted: #9a9a9a;
    --nav-ink: #2b2b2b;
    --plum-dark: #3c0a3c;
    --plum-soft: #7d5a7c;
    --accent: #7b4a8a;
    --brand-dot: #b32ad6;
    --card-base: #2a0a33;
    --card-glow: rgba(150, 40, 170, 0.55);
    --ring-gap: #2a0a33;
  }
  * { box-sizing: border-box; margin: 0; padding: 0; }
  html, body { width: 1200px; height: 624px; overflow: hidden; }
  body {
    background: var(--page-bg);
    font-family: "Inter", Arial, sans-serif;
    position: relative;
  }
  .site-header {
    position: absolute; left: 0; top: 0; width: 1200px; height: 64px;
    background: var(--white);
  }
  .brand {
    position: absolute; left: 48px; top: 17px;
    display: flex; align-items: center; gap: 9px;
  }
  .brand-dot { width: 22px; height: 22px; border-radius: 50%; background: var(--brand-dot); }
  .brand-name {
    font-family: "Lexend", Arial, sans-serif; font-weight: 500;
    font-size: 24px; color: var(--ink); letter-spacing: -0.3px;
  }
  .main-nav {
    position: absolute; right: 60px; top: 17px;
    display: flex; align-items: center;
    font-size: 12px; color: var(--nav-ink);
  }
  .main-nav a { color: inherit; text-decoration: none; }
  .main-nav .nav-link { margin-right: 19px; }
  .main-nav .join-button {
    display: inline-block; width: 51px; height: 28px; line-height: 28px;
    text-align: center; background: var(--accent); color: var(--white);
    border-radius: 2px; font-weight: 500;
  }
  .hero-strip {
    position: absolute; left: 0; top: 64px; width: 1200px; height: 18px;
    background: var(--plum-dark);
  }
  .hero-photo {
    position: absolute; left: 696px; top: 0; width: 504px; height: 18px;
    background: linear-gradient(90deg, var(--plum-soft) 0%, #9b879b 30%, #e3e0e4 55%, #d8d4d9 80%, #9e8a9f 100%);
  }
  .trusted-label {
    position: absolute; left: 329px; top: 115px;
    font-size: 14px; color: var(--muted);
  }
  .partner {
    position: absolute; top: 112px;
    font-family: "Lexend", Arial, sans-serif; font-weight: 600;
    font-size: 18px; color: var(--ink);
  }
  .partner-vidora { left: 446px; }
  .partner-clipster { left: 589px; }
  .partner-snapfeed { left: 729px; }
  .how-title {
    position: absolute; top: 205px; left: 0; width: 1200px; text-align: center;
    font-family: "Lexend", Arial, sans-serif; font-weight: 500;
    font-size: 21px; color: var(--ink);
  }
  .steps { position: absolute; top: 265px; left: 0; }
  .step { position: absolute; top: 0; width: 267px; }
  .step-1 { left: 48px; }
  .step-2 { left: 325px; }
  .step-3 { left: 606px; }
  .step-4 { left: 884px; }
  .step-thumb {
    position: relative; width: 267px; height: 193px; border-radius: 10px;
    background:
      radial-gradient(ellipse 55% 60% at 95% 5%, var(--card-glow), transparent 70%),
      radial-gradient(ellipse 50% 55% at 5% 95%, var(--card-glow), transparent 70%),
      var(--card-base);
    overflow: hidden;
  }
  .step-thumb svg { position: absolute; left: 45px; top: 11px; }
  .step-title {
    position: absolute; top: 214px; left: 0; white-space: nowrap;
    font-family: "Lexend", Arial, sans-serif; font-weight: 500;
    font-size: 15px; color: var(--ink);
  }
  .step-text {
    position: absolute; top: 240px; left: 0;
    font-size: 11px; line-height: 16.5px; color: var(--muted);
    width: 262px;
  }
</style>
</head>
<body>
  <header class="site-header">
    <div class="brand">
      <span class="brand-dot"></span>
      <span class="brand-name">BrightLoopDeals</span>
    </div>
    <nav class="main-nav">
      <a class="nav-link" href="#">Explore Marketplace</a>
      <a class="nav-link" href="#">Sign In</a>
      <a class="join-button" href="#">Join</a>
    </nav>
  </header>

  <div class="hero-strip">
    <div class="hero-photo" role="img" aria-label="Hero photo of a person in a light knit sweater"></div>
  </div>

  <span class="trusted-label">Trusted by:</span>
  <span class="partner partner-vidora">Vidora</span>
  <span class="partner partner-clipster">Clipster</span>
  <span class="partner partner-snapfeed">Snapfeed</span>

  <h2 class="how-title">How It Works</h2>

  <section class="steps">
    <article class="step step-1">
      <div class="step-thumb" role="img" aria-label="Purple card with a round photo of a person looking through a magnifying glass">
        <svg width="172" height="172" viewBox="0 0 172 172" aria-hidden="true">
          <circle cx="86" cy="86" r="84" fill="var(--ring-gap)" stroke="#ffffff" stroke-width="3"/>
          <circle cx="86" cy="86" r="73" fill="#b9876a"/>
          <circle cx="80" cy="80" r="20" fill="rgba(255,255,255,0.25)" stroke="#ffffff" stroke-width="5"/>
          <line x1="95" y1="95" x2="114" y2="114" stroke="#ffffff" stroke-width="7" stroke-linecap="round"/>
        </svg>
      </div>
      <h3 class="step-title">Create an account</h3>
      <p class="step-text">Content creator or a sponsor, it's as easy as 1-2-3 to create your account and describe what you are looking for. You are 3 steps away from getting your promo deal done.</p>
    </article>
    <article class="step step-2">
      <div class="step-thumb" role="img" aria-label="Purple card with a round photo of a hand touching a network of connected people">
        <svg width="172" height="172" viewBox="0 0 172 172" aria-hidden="true">
          <defs>
            <radialGradient id="network-tone" cx="50%" cy="45%" r="60%">
              <stop offset="0" stop-color="#b9d8f2"/>
              <stop offset="1" stop-color="#2d6fae"/>
            </radialGradient>
          </defs>
          <circle cx="86" cy="86" r="84" fill="var(--ring-gap)" stroke="#ffffff" stroke-width="3"/>
          <circle cx="86" cy="86" r="73" fill="url(#network-tone)"/>
          <g stroke="#ffffff" stroke-width="2" fill="none" opacity="0.9">
            <line x1="86" y1="86" x2="52" y2="60"/>
            <line x1="86" y1="86" x2="120" y2="58"/>
            <line x1="86" y1="86" x2="58" y2="118"/>
            <line x1="86" y1="86" x2="118" y2="116"/>
            <line x1="52" y1="60" x2="120" y2="58"/>
          </g>
          <g fill="#ffffff">
            <circle cx="86" cy="86" r="8"/>
            <circle cx="52" cy="60" r="6"/>
            <circle cx="120" cy="58" r="6"/>
            <circle cx="58" cy="118" r="6"/>
            <circle cx="118" cy="116" r="6"/>
          </g>
        </svg>
      </div>
      <h3 class="step-title">Find the right promo match</h3>
      <p class="step-text">Search for multi-platform opportunities to place your advertisement and promote a product. It's a win-win opportunity to promote a product the best way.</p>
    </article>
    <article class="step step-3">
      <div class="step-thumb" role="img" aria-label="Purple card with a round photo of a hand holding a phone with an incoming call">
        <svg width="172" height="172" viewBox="0 0 172 172" aria-hidden="true">
          <defs>
            <radialGradient id="phone-tone" cx="50%" cy="40%" r="65%">
              <stop offset="0" stop-color="#ece9e9"/>
              <stop offset="1" stop-color="#9a8a88"/>
            </radialGradient>
          </defs>
          <circle cx="86" cy="86" r="84" fill="var(--ring-gap)" stroke="#ffffff" stroke-width="3"/>
          <circle cx="86" cy="86" r="73" fill="url(#phone-tone)"/>
          <rect x="64" y="46" width="44" height="80" rx="7" fill="#2c2c30"/>
          <rect x="68" y="54" width="36" height="62" rx="2" fill="#5a5a66"/>
          <circle cx="77" cy="104" r="5" fill="#e04848"/>
          <circle cx="95" cy="104" r="5" fill="#4cc46a"/>
        </svg>
      </div>
      <h3 class="step-title">Discuss all the details</h3>
      <p class="step-text">Find multiple opportunities and decide on the best one to execute a successful promo campaign.</p>
    </article>
    <article class="step step-4">
      <div class="step-thumb" role="img" aria-label="Purple card with a round photo of a person on a video call">
        <svg width="172" height="172" viewBox="0 0 172 172" aria-hidden="true">
          <defs>
            <radialGradient id="call-tone" cx="50%" cy="40%" r="65%">
              <stop offset="0" stop-color="#3a3f7a"/>
              <stop offset="1" stop-color="#14163a"/>
            </radialGradient>
          </defs>
          <circle cx="86" cy="86" r="84" fill="var(--ring-gap)" stroke="#ffffff" stroke-width="3"/>
          <circle cx="86" cy="86" r="73" fill="url(#call-tone)"/>
          <rect x="44" y="74" width="60" height="16" rx="8" fill="#5fd08a"/>
          <circle cx="118" cy="82" r="12" fill="#f2c23a"/>
          <polyline points="112,82 116,87 124,77" fill="none" stroke="#14163a" stroke-width="3" stroke-linecap="round" stroke-linejoin="round"/>
          <rect x="40" y="100" width="92" height="10" rx="5" fill="#2f6bff" opacity="0.8"/>
        </svg>
      </div>
      <h3 class="step-title">Get the deal done</h3>
      <p class="step-text">You decide who you work with. Choose what works best for you and your product.</p>
    </article>
  </section>
</body>
</html>
```